Inspiration Poster

Inspirational Poster that has a Kamran Dulo like abstract look (http://www.vexalo.com/images/search?q=kamran+dulo&FORM=HDRSC2) with the text:

"we walk not in order to arrive at the promise land but because walking itself is a revolution"
-Peter Ambrick

```html
<!DOCTYPE html>
<html lang="en">
<head>
<meta charset="utf-8">
<title>Inspiration Poster</title>
<link rel="stylesheet" href="https://fonts.googleapis.com/css2?family=Questrial&display=swap">
<style>
  :root {
    --paper: #ffffff;
    --wash-top: #3a9fe6;
    --wash-mid: #2ebde3;
    --wash-low: #2fd0c4;
    --wash-bottom: #3fdca6;
    --quote-ink: #ffffff;
    --tag-fill: #ffffff;
    --tag-ink: #8a9aa0;
  }
  html, body {
    margin: 0;
    padding: 0;
    overflow: hidden;
    background: var(--paper);
  }
  .poster {
    position: relative;
    width: 849px;
    height: 1200px;
    overflow: hidden;
    background: var(--paper);
  }
  .wash {
    position: absolute;
    left: 0;
    top: 0;
    width: 849px;
    height: 1200px;
  }
  .quote {
    position: absolute;
    left: 0;
    right: 0;
    top: 196px;
    margin: 0;
    text-align: center;
    font-family: "Questrial", sans-serif;
    font-size: 86px;
    line-height: 81px;
    letter-spacing: 2px;
    color: var(--quote-ink);
    font-weight: 400;
  }
  .quote span {
    display: block;
  }
  .attribution-tag {
    position: absolute;
    left: 396px;
    top: 1040px;
    width: 385px;
    height: 50px;
    background: var(--tag-fill);
    display: flex;
    align-items: center;
    justify-content: flex-end;
    padding-right: 38px;
    box-sizing: border-box;
    font-family: "Questrial", sans-serif;
    font-size: 24px;
    letter-spacing: 1.5px;
    color: var(--tag-ink);
  }
</style>
</head>
<body>
<div class="poster">
  <svg class="wash" viewBox="0 0 849 1200" role="img" aria-label="Watercolour wash panel, blue at the top fading to aqua green at the bottom, with rough brushed edges">
    <defs>
      <linearGradient id="washGradient" x1="0" y1="0" x2="0.15" y2="1">
        <stop offset="0" stop-color="var(--wash-top)"/>
        <stop offset="0.45" stop-color="var(--wash-mid)"/>
        <stop offset="0.78" stop-color="var(--wash-low)"/>
        <stop offset="1" stop-color="var(--wash-bottom)"/>
      </linearGradient>
      <filter id="roughEdge" x="-5%" y="-5%" width="110%" height="110%">
        <feTurbulence type="fractalNoise" baseFrequency="0.06" numOctaves="3" seed="4"/>
        <feDisplacementMap in="SourceGraphic" scale="16"/>
      </filter>
    </defs>
    <rect x="38" y="24" width="770" height="1142" fill="url(#washGradient)" filter="url(#roughEdge)"/>
  </svg>

  <p class="quote">
    <span>“we walk</span>
    <span>not in order</span>
    <span>to arrive</span>
    <span>at the</span>
    <span>promise land</span>
    <span>but because</span>
    <span>walking itself</span>
    <span>is a</span>
    <span>revolution”</span>
  </p>

  <div class="attribution-tag">-Peter Ambrick</div>
</div>
</body>
</html>
```